Business Card & Letterhead

We are a Raw, Vegan, Organic dessert company in Australia.

We require a new look Business Card and letterhead. Currently we are re-branding and therefore need designs to fit the new look.

Our signature Blue color is definitely still a preference to have as a dominant color in your design.

The feel of the brand is fresh, quirky and healthy. Provide your best design that you believe fits our brand.

Visit our website [login to view URL] and instagram to get a feel for the company branding and feel.

Please provide creative and original designs, do not copy each others designs.

Final files must be submitted as PSD LAYERED FILES
with editable text.

View the very old designs in the below dropbox folder:

```html
<!DOCTYPE html>
<html lang="en">
<head>
<meta charset="utf-8">
<title>Purebite Treats – Letterhead &amp; Business Cards</title>
<link href="https://fonts.googleapis.com/css2?family=Raleway:wght@300&family=Open+Sans:ital,wght@0,400;0,600;1,400&display=swap" rel="stylesheet">
<style>
  :root{
    --backdrop:#e4e0e1;
    --paper:#ffffff;
    --brand-blue:#86c3df;
    --brand-gold:#c9a86a;
    --gold-soft:#efdcb8;
    --ink:#4a4a4a;
    --ink-soft:#7a7a7a;
  }
  *{box-sizing:border-box;margin:0;padding:0}
  html,body{width:1200px;height:960px;overflow:hidden}
  body{background:var(--backdrop);font-family:"Open Sans",Arial,sans-serif;color:var(--ink);position:relative}

  .brand-name{font-family:"Raleway",Arial,sans-serif;font-weight:300;color:var(--brand-gold);letter-spacing:1px;white-space:nowrap}

  /* Letterhead */
  .letterhead{position:absolute;left:90px;top:100px;width:540px;height:760px;background:var(--paper);box-shadow:0 6px 18px rgba(0,0,0,.12)}
  .letterhead__band-top{position:absolute;left:0;top:0;width:340px;height:26px;background:var(--brand-blue)}
  .letterhead__band-bottom{position:absolute;left:0;bottom:0;width:100%;height:70px;background:var(--brand-blue)}
  .letterhead__brand{position:absolute;left:100px;top:60px;font-size:30px;line-height:36px}
  .letterhead__contact{position:absolute;left:392px;top:60px;width:130px;font-size:7.5px;line-height:11px;color:var(--ink-soft)}
  .letterhead__body{position:absolute;left:56px;top:180px;width:430px;font-size:9.5px;line-height:15px}
  .letterhead__body p{margin-bottom:14px}
  .letterhead__signature{position:absolute;left:56px;top:600px;width:150px;border-top:1.5px solid var(--ink);text-align:center;font-size:10px;padding-top:4px}

  /* Business cards */
  .card{position:absolute;width:440px;height:252px;background:var(--paper);box-shadow:0 6px 16px rgba(0,0,0,.14);overflow:hidden}
  .card--front{left:680px;top:150px}
  .card--back{left:680px;top:470px}

  .card--front .brand-name{position:absolute;left:40px;top:30px;font-size:32px}
  .card__tagline{position:absolute;left:40px;top:78px;font-size:11px;font-style:italic;color:var(--ink-soft)}
  .card__contacts{position:absolute;left:240px;top:96px;list-style:none;font-size:9px;line-height:15px;color:var(--ink-soft)}
  .card__contacts li{display:flex;align-items:center;gap:6px}
  .card__contacts svg{width:9px;height:9px;fill:var(--ink-soft)}
  .card__stripe{position:absolute;left:0;width:100%}
  .card__stripe--gold{top:178px;height:3px;background:var(--brand-gold)}
  .card__stripe--cream{top:184px;height:16px;background:var(--gold-soft)}
  .card__stripe--blue{bottom:0;height:22px;background:var(--brand-blue)}
  .card__person{position:absolute;left:40px;top:140px;font-size:11px;line-height:14px}
  .card__role{font-size:9px;color:var(--ink-soft)}

  .card__band{position:absolute;left:0;top:0;width:100%;height:120px;background:var(--brand-blue)}
  .card--back .brand-name{position:absolute;left:0;width:100%;text-align:center;top:48px;font-size:36px;color:var(--paper)}
  .card__values{position:absolute;left:0;top:150px;width:100%;display:flex;justify-content:center;gap:54px;list-style:none}
  .card__values li{display:flex;flex-direction:column;align-items:center;gap:6px;font-size:9px;letter-spacing:1px;color:var(--ink-soft)}
  .card__values svg{width:20px;height:20px}
</style>
</head>
<body>

<section class="letterhead">
  <div class="letterhead__band-top"></div>
  <div class="letterhead__brand brand-name">Purebite Treats</div>
  <div class="letterhead__contact">
    0400 123 456<br>
    hello@purebitetreats.com.au<br>
    www.purebitetreats.com.au<br>
    facebook.com/purebitetreats
  </div>
  <div class="letterhead__body">
    <p>Tomas Varga<br>Dear :</p>
    <p>Lorem ipsum dolor sit amet, consectetur adipiscing elit. Aenean ut ipsum eget massa hendrerit vestibulum vel in velit. Donec pretium neque velit.</p>
    <p>Aliquam porta lectus nec mauris ornare venenatis. Vivamus non est turpis, et cursus sem. Mauris vehicula erat in diam auctor at bibendum nisl lacinia.</p>
    <p>Morbi imperdiet neque vehicula nunc convallis gravida. Vestibulum iaculis pretium placerat. Integer consequat, est sit amet facilisis eleifend, nibh nibh varius orci, eget dapibus arcu dui non purus. Pellentesque in magna mauris. Duis enim sapien, dictum vitae condimentum a, pulvinar vel lacus. Mauris et molestie nibh. Vestibulum vitae nulla at metus elementum porta sit amet interdum elit. Nulla sollicitudin neque eu nulla volutpat congue.</p>
    <p>Etiam pellentesque, velit id dapibus fermentum, turpis sapien ornare dui, ac tincidunt ligula odio congue purus. Nunc sed ante dui, in porta lectus. Cras nec sem lorem. In hac habitasse platea dictumst. Maecenas id diam quis dui porta tristique. Sed id egestas felis. Donec ullamcorper mattis posuere. Phasellus fermentum eleifend tortor vel dapibus. Vestibulum ante ipsum.</p>
  </div>
  <div class="letterhead__signature">Signature</div>
  <div class="letterhead__band-bottom"></div>
</section>

<section class="card card--front">
  <div class="brand-name">Purebite Treats</div>
  <div class="card__tagline">treats made the fresh raw way</div>
  <ul class="card__contacts">
    <li><svg viewBox="0 0 10 10"><path d="M2 0h2l1 3-1.5 1a6 6 0 0 0 2.5 2.5L7 5l3 1v2a2 2 0 0 1-2 2A8 8 0 0 1 0 2a2 2 0 0 1 2-2z"/></svg>0400 123 456</li>
    <li><svg viewBox="0 0 10 10"><path d="M0 2h10v6H0z M0 2l5 3.5L10 2" fill="none" stroke="#7a7a7a"/></svg>hello@purebitetreats.com.au</li>
    <li><svg viewBox="0 0 10 10"><circle cx="5" cy="5" r="4.3" fill="none" stroke="#7a7a7a"/></svg>www.purebitetreats.com.au</li>
    <li><svg viewBox="0 0 10 10"><rect width="10" height="10" rx="2"/></svg>facebook.com/purebitetreats</li>
  </ul>
  <div class="card__person">Tomas Varga<br><span class="card__role">CEO/Founder</span></div>
  <div class="card__stripe card__stripe--gold"></div>
  <div class="card__stripe card__stripe--cream"></div>
  <div class="card__stripe card__stripe--blue"></div>
</section>

<section class="card card--back">
  <div class="card__band"></div>
  <div class="brand-name">Purebite Treats</div>
  <ul class="card__values">
    <li><svg viewBox="0 0 20 20"><circle cx="10" cy="10" r="8" fill="var(--brand-blue)"/></svg>RAW</li>
    <li><svg viewBox="0 0 20 20"><circle cx="10" cy="10" r="8" fill="var(--brand-blue)"/></svg>VEGAN</li>
    <li><svg viewBox="0 0 20 20"><circle cx="10" cy="10" r="8" fill="var(--brand-blue)"/></svg>ORGANIC</li>
  </ul>
</section>

</body>
</html>
```